Kestrel Path Business card

We are a company that owns 2 compliance software programs for TV, Radio and Cable industries as well as an online job board. We need a professional business card that incorproates all three logos.

```html
<!DOCTYPE html>
<html lang="en">
<head>
<meta charset="utf-8">
<title>Kestrel Path Business Card</title>
<link href="https://fonts.googleapis.com/css2?family=Roboto:wght@400;500;700&family=Montserrat:wght@700&display=swap" rel="stylesheet">
<style>
  :root {
    --red: #e5331f;
    --navy: #141456;
    --blue: #2b8fd8;
    --paper: #f7f7f5;
    --stage: #2a2a2c;
    --white: #ffffff;
  }
  * { box-sizing: border-box; margin: 0; padding: 0; }
  html, body { width: 1200px; height: 874px; overflow: hidden; }
  body {
    background: var(--stage);
    font-family: "Roboto", Arial, sans-serif;
    position: relative;
  }
  .card {
    position: absolute;
    left: 280px;
    width: 640px;
    height: 366px;
    overflow: hidden;
  }
  .card-front { top: 51px; background: var(--red); }
  .card-back { top: 457px; background: var(--paper); }

  .brand-row {
    position: absolute;
    display: flex;
    align-items: center;
    gap: 18px;
  }
  .card-front .brand-row { left: 0; right: 0; top: 140px; justify-content: center; }
  .card-back .brand-row { left: 0; right: 0; top: 58px; justify-content: center; }

  .brand {
    display: flex;
    align-items: center;
    gap: 7px;
    font-family: "Montserrat", Arial, sans-serif;
    font-weight: 700;
    font-size: 19px;
    line-height: 1;
    white-space: nowrap;
  }
  .brand-mark { width: 14px; height: 14px; flex: none; }
  .brand-mark.round { border-radius: 50%; }
  .divider { width: 2px; height: 54px; }

  .card-front .brand { color: var(--white); }
  .card-front .brand-mark { background: var(--white); }
  .card-front .divider { background: var(--white); }

  .card-back .brand-broadcast, .card-back .brand-cable { color: var(--navy); }
  .card-back .brand-broadcast .brand-mark, .card-back .brand-cable .brand-mark { background: var(--red); }
  .card-back .brand-jobs { color: var(--blue); }
  .card-back .brand-jobs .brand-mark { background: var(--blue); }
  .card-back .divider { background: var(--navy); }

  .web-address {
    position: absolute;
    left: 0; right: 0; bottom: 62px;
    text-align: center;
    color: var(--white);
    font-size: 16px;
    letter-spacing: 9px;
  }

  .name-band {
    position: absolute;
    left: 0; top: 188px;
    width: 360px; height: 118px;
    background: var(--navy);
    color: var(--white);
    padding: 16px 0 0 44px;
  }
  .person-name { font-size: 25px; font-weight: 700; letter-spacing: 0.5px; }
  .person-title { font-size: 17px; margin-top: 2px; }
  .person-address { font-size: 16px; margin-top: 8px; line-height: 1.3; }

  .contact-band {
    position: absolute;
    left: 340px; top: 258px;
    width: 276px; height: 108px;
    background: var(--red);
    color: var(--white);
    padding: 14px 18px 0 0;
  }
  .contact-list { list-style: none; }
  .contact-list li {
    display: flex;
    justify-content: flex-end;
    align-items: center;
    gap: 10px;
    font-size: 15px;
    line-height: 22px;
  }
  .contact-icon { width: 13px; height: 13px; flex: none; }
</style>
</head>
<body>

<section class="card card-front" aria-label="Card front">
  <div class="brand-row">
    <div class="brand brand-broadcast"><span class="brand-mark"></span>Kestrel Broadcast</div>
    <span class="divider"></span>
    <div class="brand brand-cable"><span class="brand-mark"></span>Kestrel Cable</div>
    <span class="divider"></span>
    <div class="brand brand-jobs"><span class="brand-mark round"></span>CrewBoard.com</div>
  </div>
  <p class="web-address">www.kestrelpath.com</p>
</section>

<section class="card card-back" aria-label="Card back">
  <div class="brand-row">
    <div class="brand brand-broadcast"><span class="brand-mark"></span>Kestrel Broadcast</div>
    <span class="divider"></span>
    <div class="brand brand-cable"><span class="brand-mark"></span>Kestrel Cable</div>
    <span class="divider"></span>
    <div class="brand brand-jobs"><span class="brand-mark round"></span>CrewBoard.com</div>
  </div>

  <div class="name-band">
    <h1 class="person-name">DANA WHITLOW</h1>
    <p class="person-title">CEO/FOUNDER</p>
    <p class="person-address">4120 Alder Court<br>Fairbanks, Alaska 99701</p>
  </div>

  <div class="contact-band">
    <ul class="contact-list">
      <li>555 014 2291
        <svg class="contact-icon" viewBox="0 0 16 16" aria-hidden="true"><path fill="#fff" d="M3 1l3 3-1.6 1.8c.9 2 2.6 3.7 4.8 4.8L11 9l3 3-2 2.5C6.5 14 2 9.5 1.5 3z"/></svg>
      </li>
      <li>555 017 3308
        <svg class="contact-icon" viewBox="0 0 16 16" aria-hidden="true"><rect x="4" y="1" width="8" height="14" rx="1.5" fill="none" stroke="#fff" stroke-width="1.6"/><circle cx="8" cy="12.5" r="0.9" fill="#fff"/></svg>
      </li>
      <li>555 019 4472
        <svg class="contact-icon" viewBox="0 0 16 16" aria-hidden="true"><rect x="4" y="1" width="8" height="5" fill="none" stroke="#fff" stroke-width="1.4"/><rect x="1" y="6" width="14" height="6" rx="1" fill="#fff"/><rect x="4" y="10" width="8" height="5" fill="#fff" stroke="#e5331f" stroke-width="1"/></svg>
      </li>
      <li>dana@kestrelpath.com
        <svg class="contact-icon" viewBox="0 0 16 16" aria-hidden="true"><rect x="1" y="3" width="14" height="10" fill="#fff"/><path d="M1 3l7 6 7-6" fill="none" stroke="#e5331f" stroke-width="1.3"/></svg>
      </li>
    </ul>
  </div>
</section>

</body>
</html>
```